Timber Ridge Land Services Business Cards

Need to create a business card with the company logo "Timber Ridge Land Services". The business will provide forestry mulching for land clearing and vegetation control, brush and small tree removal, wildlife habitat improvement and trail and property access creation.

```html
<!DOCTYPE html>
<html lang="en">
<head>
<meta charset="UTF-8">
<title>Timber Ridge Land Services – Business Card</title>
<link href="https://fonts.googleapis.com/css2?family=Lato:wght@400;700;900&display=swap" rel="stylesheet">
<style>
  :root {
    --page-bg: #8a8a8a;
    --card-bg: #ffffff;
    --brand-green: #0f5a33;
    --bullet-green: #46a84c;
    --accent-yellow: #f3e95b;
    --text-gray: #585858;
    --text-dark: #2b2b2b;
  }
  * { margin: 0; padding: 0; box-sizing: border-box; }
  html, body {
    width: 1200px; height: 788px; overflow: hidden;
    background: var(--page-bg);
    font-family: "Lato", Arial, sans-serif;
  }
  .card {
    position: absolute; left: 40px; top: 58px;
    width: 1120px; height: 672px;
    background: var(--card-bg);
    overflow: hidden;
    box-shadow: 0 6px 18px rgba(0,0,0,0.35);
  }
  .card-art { position: absolute; inset: 0; width: 100%; height: 100%; }
  .brand-name {
    position: absolute; left: 70px; top: 84px;
    color: var(--brand-green); font-weight: 900;
    line-height: 1.05; text-transform: uppercase;
  }
  .brand-name .line-main { display: block; font-size: 44px; letter-spacing: 0.5px; }
  .brand-name .line-sub { display: block; font-size: 24px; letter-spacing: 2px; }
  .services {
    position: absolute; left: 66px; top: 240px; width: 530px;
    list-style: none;
  }
  .services li {
    position: relative; padding-left: 26px; margin-bottom: 17px;
    font-size: 21px; font-weight: 700; letter-spacing: 0.6px;
    line-height: 1.15; color: var(--text-gray); text-transform: uppercase;
  }
  .services li::before {
    content: ""; position: absolute; left: 0; top: 5px;
    width: 15px; height: 15px; border-radius: 50%;
    background: var(--bullet-green);
  }
  .cta {
    position: absolute; left: 62px; top: 442px;
    width: 490px; height: 146px;
    border: 3px solid var(--accent-yellow); border-radius: 8px;
    text-align: center; color: var(--text-dark);
  }
  .cta-text {
    margin-top: 18px; font-size: 28px; line-height: 1.3; letter-spacing: 0.5px;
    text-transform: uppercase;
  }
  .cta-text strong { color: var(--brand-green); font-weight: 900; }
  .phone-pill {
    position: absolute; left: 134px; top: 552px;
    width: 350px; height: 64px; border-radius: 32px;
    background: var(--accent-yellow);
    display: flex; align-items: center;
  }
  .phone-icon {
    width: 56px; height: 56px; margin-left: 4px; border-radius: 50%;
    background: var(--brand-green); display: flex; align-items: center; justify-content: center;
  }
  .phone-number {
    margin-left: 28px; font-size: 31px; font-weight: 900;
    color: var(--text-dark); letter-spacing: 1px;
  }
</style>
</head>
<body>
  <div class="card">
    <svg class="card-art" viewBox="0 0 400 240" preserveAspectRatio="none">
      <defs>
        <linearGradient id="foliage" x1="0" y1="0" x2="1" y2="1">
          <stop offset="0" stop-color="#2b2f22"/>
          <stop offset="0.45" stop-color="#4f5a2c"/>
          <stop offset="1" stop-color="#6f7a30"/>
        </linearGradient>
      </defs>
      <polygon class="edge-stripe" points="168,0 400,0 400,240 206,240 251,88" fill="var(--accent-yellow)"/>
      <g role="img" aria-label="Photo of a young deer in woodland beside hedge shears trimming green shrubs">
        <polygon class="photo-area" points="174,0 400,0 400,240 213,240 258,88" fill="url(#foliage)"/>
      </g>
      <line class="photo-divider" x1="349" y1="0" x2="316" y2="150" stroke="var(--accent-yellow)" stroke-width="2.5"/>
    </svg>

    <div class="brand-name">
      <span class="line-main">Timber Ridge</span>
      <span class="line-sub">Land Services</span>
    </div>

    <ul class="services">
      <li>Forestry mulching for land clearing<br>and vegetation control</li>
      <li>Brush and small tree removal</li>
      <li>Wildlife habitat improvement and trail<br>and property access creation</li>
    </ul>

    <div class="cta">
      <p class="cta-text">Call us for a<br><strong>Free</strong> estimate today!</p>
    </div>

    <div class="phone-pill">
      <div class="phone-icon">
        <svg width="28" height="28" viewBox="0 0 24 24" aria-hidden="true">
          <path fill="#ffffff" d="M6.6 10.8c1.4 2.8 3.8 5.1 6.6 6.6l2.2-2.2c.3-.3.7-.4 1-.2 1.1.4 2.3.6 3.6.6.6 0 1 .4 1 1V20c0 .6-.4 1-1 1C10.6 21 3 13.4 3 4c0-.6.4-1 1-1h3.5c.6 0 1 .4 1 1 0 1.3.2 2.5.6 3.6.1.3 0 .7-.2 1z"/>
        </svg>
      </div>
      <span class="phone-number">123-456-7890</span>
    </div>
  </div>
</body>
</html>
```